Business Card Design

Contact Information for Business Card

A vertical business card request- a medium & light gray with silverfern tree logo (logo is attached)

Please use Trebuchet font -- if possible- can we use two different color gray? (See pictures attached below)
Info on the front should be the Silverfern tree logo - on the top of the card, followed by the info ...
Card to read: " " indicated what should be on the card --
Name: " Joan Pelley "
Title : "Partner "
" Office: 202.555.0147 "
" Mobile: 202.555.0182 "

Backside of the card - solid medium color gray color w/ address and small message centered in the card - Trebuchet font
to read:

" 317 B North Linden Avenue, NE "
" Washington, DC 20099 "

Then below address to read:
" Fundraising | Event Planning | Political Consulting "

```html
<!DOCTYPE html>
<html lang="en">
<head>
<meta charset="utf-8">
<title>Silverfern Strategies — Business Card</title>
<link rel="stylesheet" href="https://fonts.googleapis.com/css2?family=Cabin:wght@400;600&display=swap">
<style>
  :root {
    --backdrop: #e4e2df;
    --card-gray: #5f6062;
    --card-white: #ffffff;
    --ink-dark: #1c1c1c;
    --ink-light: #f2f2f2;
    --wordmark-gray: #d6d6d6;
    --card-w: 340px;
    --card-h: 595px;
  }
  * { box-sizing: border-box; margin: 0; padding: 0; }
  html, body {
    width: 1200px;
    height: 775px;
    overflow: hidden;
    background: var(--backdrop);
    font-family: "Trebuchet MS", "Cabin", sans-serif;
  }
  .sheet {
    width: 1200px;
    height: 775px;
    display: flex;
    justify-content: center;
    align-items: center;
    gap: 90px;
  }
  .card {
    width: var(--card-w);
    height: var(--card-h);
    box-shadow: 0 6px 18px rgba(0, 0, 0, 0.18);
    overflow: hidden;
    display: flex;
    flex-direction: column;
  }

  /* Front */
  .card-front .brand-panel {
    flex: 0 0 68%;
    background: var(--card-gray);
    display: flex;
    flex-direction: column;
    justify-content: flex-end;
    align-items: center;
    padding-bottom: 34px;
  }
  .wordmark {
    color: var(--wordmark-gray);
    font-weight: 400;
    font-size: 30px;
    letter-spacing: 2px;
    text-transform: uppercase;
    text-align: right;
    line-height: 1;
  }
  .wordmark .wordmark-sub {
    display: block;
    font-size: 16px;
    letter-spacing: 3px;
    margin-top: 4px;
  }
  .card-front .contact-panel {
    flex: 1;
    background: var(--card-white);
    color: var(--ink-dark);
    padding: 26px 0 0 48px;
  }
  .person-name {
    font-size: 17px;
    font-weight: 600;
    letter-spacing: 0.4px;
  }
  .person-title {
    font-size: 13px;
    margin-top: 4px;
    margin-left: 4px;
  }
  .contact-lines {
    list-style: none;
    margin-top: 28px;
    margin-left: 4px;
    font-size: 14px;
    line-height: 1.35;
  }
  .contact-lines .email { margin-bottom: 8px; }
  .contact-lines .label { font-size: 12px; margin-left: 4px; }

  /* Back */
  .card-back {
    background: var(--card-gray);
    color: var(--ink-light);
    justify-content: flex-end;
    align-items: center;
    text-align: center;
    padding-bottom: 118px;
  }
  .address {
    font-style: normal;
    font-size: 13px;
    line-height: 1.3;
    letter-spacing: 0.3px;
  }
  .services {
    margin-top: 38px;
    font-size: 11.5px;
    letter-spacing: 0.3px;
  }
</style>
</head>
<body>
  <main class="sheet">
    <section class="card card-front" aria-label="Card front">
      <div class="brand-panel">
        <p class="wordmark">Silverfern<span class="wordmark-sub">Strategies</span></p>
      </div>
      <div class="contact-panel">
        <h1 class="person-name">Joan Pelley</h1>
        <p class="person-title">Partner</p>
        <ul class="contact-lines">
          <li class="email">joan@silverfernllc.com</li>
          <li>202.555.0182 <span class="label">mobile</span></li>
          <li>202.555.0147 <span class="label">office</span></li>
        </ul>
      </div>
    </section>

    <section class="card card-back" aria-label="Card back">
      <address class="address">
        317 B North Linden Avenue, NE<br>
        Washington, DC 20099
      </address>
      <p class="services">Fundraising | Event Planning | Political Consulting</p>
    </section>
  </main>
</body>
</html>
```